Eye catching Stationary Design

Healthcare consultant firm looking for stationary design ( letterhead, envelope and business cards) That’s professional, classy and eye catching . The design should incorporate the logo and the colors of the logo in its design. You can see the logo on our website at www crestmore advisory. net.

```html
<!DOCTYPE html>
<html lang="en">
<head>
<meta charset="utf-8">
<title>Crestmore Advisory – Stationery Set</title>
<link rel="stylesheet" href="https://fonts.googleapis.com/css2?family=Cinzel:wght@500&family=Montserrat:wght@400;600&display=swap">
<style>
  :root {
    --navy: #0b57a4;
    --sky: #35a7db;
    --ink: #333a40;
    --paper: #ffffff;
    --backdrop: #e9e6e1;
  }
  * { box-sizing: border-box; margin: 0; padding: 0; }
  html, body { width: 1200px; height: 1200px; overflow: hidden; }
  body {
    position: relative;
    background: var(--backdrop);
    font-family: "Montserrat", Arial, sans-serif;
    color: var(--ink);
  }
  .sheet {
    position: absolute;
    background: var(--paper);
    box-shadow: 0 4px 14px rgba(0,0,0,0.18);
    overflow: hidden;
  }
  .brand-name {
    font-family: "Cinzel", Georgia, serif;
    font-weight: 500;
    color: var(--navy);
    white-space: nowrap;
    letter-spacing: 0.5px;
  }
  .contact-band {
    position: absolute;
    left: 0; right: 0;
    background: var(--navy);
    color: #fff;
    display: flex;
    flex-direction: column;
    justify-content: center;
  }
  .contact-line {
    display: flex;
    align-items: center;
    white-space: nowrap;
  }
  .contact-line .sep { margin: 0 0.6em; opacity: 0.8; }
  .icon { flex: none; margin-right: 0.45em; }
  .web-band {
    position: absolute;
    left: 0; right: 0;
    background: var(--sky);
    color: var(--navy);
    font-weight: 600;
    display: flex;
    align-items: center;
  }

  /* Letterhead */
  .letterhead { left: 138px; top: 205px; width: 575px; height: 813px; }
  .letterhead .brand-name {
    position: absolute; left: 0; right: 0; top: 70px;
    text-align: center; font-size: 22px;
  }
  .letterhead .contact-band { top: 709px; height: 45px; padding-left: 19px; font-size: 11px; gap: 5px; }
  .letterhead .web-band { top: 765px; height: 20px; padding-left: 19px; font-size: 11px; }

  /* Envelope */
  .envelope { left: 480px; top: 612px; width: 641px; height: 278px; }
  .envelope .brand-name { position: absolute; left: 22px; top: 70px; font-size: 18px; }
  .envelope .contact-band { top: 176px; height: 45px; padding-left: 22px; font-size: 12px; gap: 5px; }
  .envelope .web-band { top: 230px; height: 22px; padding-left: 22px; font-size: 11px; }

  /* Business cards */
  .card { left: 802px; width: 231px; height: 132px; }
  .card-front { top: 228px; }
  .card-front .brand-name {
    position: absolute; left: 0; right: 0; top: 56px;
    text-align: center; font-size: 11.5px;
  }
  .card-back { top: 409px; }
  .card-back .contact-band {
    top: 0; height: 85px; padding: 10px 0 0 10px;
    justify-content: flex-start; font-size: 8.5px; gap: 4px;
  }
  .card-back .web-band { top: 95px; height: 14px; padding-left: 10px; font-size: 7px; }
</style>
</head>
<body>

<svg width="0" height="0" style="position:absolute">
  <defs>
    <symbol id="icon-phone" viewBox="0 0 20 20">
      <circle cx="10" cy="10" r="10" fill="#35a7db"/>
      <path d="M7 5.5c.6-.3 1.1 0 1.4.6l.6 1.4c.2.5 0 .9-.4 1.2l-.5.4c.5 1.1 1.4 2 2.5 2.5l.4-.5c.3-.4.7-.6 1.2-.4l1.4.6c.6.3.9.8.6 1.4-.5 1.1-1.5 1.6-2.6 1.3C9.3 13.8 6.2 10.7 5.7 8.2 5.4 7 5.9 6 7 5.5z" fill="#fff"/>
    </symbol>
    <symbol id="icon-mail" viewBox="0 0 20 20">
      <circle cx="10" cy="10" r="10" fill="#35a7db"/>
      <rect x="5" y="6.5" width="10" height="7" rx="1" fill="#fff"/>
      <path d="M5.5 7l4.5 3.6L14.5 7" fill="none" stroke="#35a7db" stroke-width="1"/>
    </symbol>
    <symbol id="icon-pin" viewBox="0 0 20 20">
      <circle cx="10" cy="10" r="10" fill="#35a7db"/>
      <path d="M10 4.5a3.6 3.6 0 0 0-3.6 3.6c0 2.7 3.6 7 3.6 7s3.6-4.3 3.6-7A3.6 3.6 0 0 0 10 4.5z" fill="#fff"/>
      <circle cx="10" cy="8.1" r="1.4" fill="#35a7db"/>
    </symbol>
  </defs>
</svg>

<section class="sheet letterhead" aria-label="Letterhead">
  <div class="brand-name">Crestmore Advisory LLC</div>
  <div class="contact-band">
    <div class="contact-line">
      <svg class="icon" width="12" height="12"><use href="#icon-phone"/></svg>(555) 214-0387<span class="sep">|</span>
      <svg class="icon" width="12" height="12"><use href="#icon-mail"/></svg>info@crestmoreadvisory.net
    </div>
    <div class="contact-line">
      <svg class="icon" width="12" height="12"><use href="#icon-pin"/></svg>118 Harlow St Suite 310, Fairview, NY 10020, USA
    </div>
  </div>
  <div class="web-band">www.crestmoreadvisory.net</div>
</section>

<section class="sheet card card-front" aria-label="Business card front">
  <div class="brand-name">Crestmore Advisory LLC</div>
</section>

<section class="sheet card card-back" aria-label="Business card back">
  <div class="contact-band">
    <div class="contact-line">
      <svg class="icon" width="9" height="9"><use href="#icon-phone"/></svg>(555) 214-0387
    </div>
    <div class="contact-line">
      <svg class="icon" width="9" height="9"><use href="#icon-mail"/></svg>info@crestmoreadvisory.net
    </div>
    <div class="contact-line">
      <svg class="icon" width="9" height="9"><use href="#icon-pin"/></svg>118 Harlow St Suite 310, Fairview, NY 10020, USA
    </div>
  </div>
  <div class="web-band">www.crestmoreadvisory.net</div>
</section>

<section class="sheet envelope" aria-label="Envelope">
  <div class="brand-name">Crestmore Advisory LLC</div>
  <div class="contact-band">
    <div class="contact-line">
      <svg class="icon" width="13" height="13"><use href="#icon-phone"/></svg>(555) 214-0387<span class="sep">|</span>
      <svg class="icon" width="13" height="13"><use href="#icon-mail"/></svg>info@crestmoreadvisory.net
    </div>
    <div class="contact-line">
      <svg class="icon" width="13" height="13"><use href="#icon-pin"/></svg>118 Harlow St Suite 310, Fairview, NY 10020, USA
    </div>
  </div>
  <div class="web-band">www.crestmoreadvisory.net</div>
</section>

</body>
</html>
```